Realty Group Needs Classy, Contemporary Letterhead Design

We need a letterhead design for a new realty company located in NY, USA. We buy investment properties to rehabilitate and or keep in our rental portfolio.

```html
<!DOCTYPE html>
<html lang="en">
<head>
<meta charset="utf-8">
<title>Meridian Realty Group – Letterhead</title>
<link href="https://fonts.googleapis.com/css2?family=Source+Sans+3:wght@400;600;800&display=swap" rel="stylesheet">
<style>
  :root{
    --backdrop:#58585a;
    --paper:#ffffff;
    --brand:#4b2a86;
    --body-text:#8b8b90;
    --footer-text:#3f3f42;
    --rule:#8a8a8c;
    --art-tint:#e4e1ef;
  }
  *{margin:0;padding:0;box-sizing:border-box}
  html,body{width:960px;height:1200px;overflow:hidden}
  body{background:var(--backdrop);font-family:"Source Sans 3",Arial,sans-serif;position:relative}
  .sheet{position:absolute;left:96px;top:58px;width:768px;height:1084px;background:var(--paper);overflow:hidden}

  .brand{position:absolute;left:0;right:0;top:96px;display:flex;justify-content:center;align-items:center;gap:9px}
  .brand-dot{width:14px;height:14px;border-radius:50%;background:var(--brand)}
  .brand-name{color:var(--brand);font-weight:800;font-size:26px;letter-spacing:.5px}

  .hero-art{position:absolute;left:88px;top:600px;width:600px;height:402px;
    background:radial-gradient(ellipse at 55% 60%,var(--art-tint) 0%,rgba(228,225,239,.65) 50%,rgba(228,225,239,0) 78%)}

  .salutation{position:absolute;left:68px;top:251px;font-size:14px;color:var(--body-text)}
  .letter-body{position:absolute;left:50px;top:316px;width:688px;color:var(--body-text);font-size:13.6px;line-height:18.5px;text-align:justify}
  .letter-body p{margin-bottom:18.5px}
  .letter-body p:first-child{text-indent:46px}

  .footer-rule{position:absolute;left:0;right:0;top:1001px;height:2px;background:var(--rule)}
  .contact{position:absolute;top:1026px;font-size:12px;line-height:15.5px;color:var(--footer-text)}
  .contact-row{display:flex;align-items:center;gap:6px}
  .contact svg{width:11px;height:11px;fill:var(--footer-text);flex:none}
  .contact-address{left:36px}
  .contact-address .indent{padding-left:17px}
  .contact-phone{left:312px}
  .contact-web{left:590px}
  .divider{position:absolute;top:1026px;width:1px;height:36px;background:var(--rule)}
</style>
</head>
<body>
<main class="sheet">
  <header class="brand">
    <span class="brand-dot"></span>
    <span class="brand-name">Meridian Realty Group, LLC</span>
  </header>

  <div class="hero-art" role="img" aria-label="Large faint lavender illustration of an archer drawing a bow, set behind the lower part of the letter"></div>

  <p class="salutation">Dear Sir</p>

  <section class="letter-body">
    <p>Lorem ipsum dolor sit amet, consectetur adipiscing elit. Integer eu odio mattis, pulvinar turpis quis, faucibus nisl. Proin feugiat, erat vitae cursus pharetra, enim est semper ligula, in malesuada orci nisl et diam. Etiam elementum metus ac fringilla vulputate. Etiam mattis ligula sed ante mollis bibendum. Orci varius natoque penatibus et magnis dis parturient montes, nascetur ridiculus mus.</p>
    <p>Ut nibh augue, blandit ac orci ac, rutrum congue enim. Suspendisse gravida vulputate felis, quis interdum orci tincidunt quis. Praesent imperdiet maximus neque. Mauris ut dui enim. Nullam at efficitur elit. Donec ante ipsum, fermentum at lectus vel, blandit vulputate ante. Proin luctus suscipit diam id vestibulum. Morbi malesuada id mauris eget ullamcorper.</p>
    <p>Donec varius orci purus, vitae aliquam libero volutpat id. Integer sed imperdiet libero. Aliquam accumsan, risus sit amet ornare consectetur, turpis felis dictum justo, non rhoncus mauris dui sed velit. Pellentesque habitant morbi tristique senectus et netus et malesuada fames ac turpis egestas. Pellentesque tincidunt vitae ligula nec imperdiet. Donec sed congue enim. Nullam elementum faucibus nulla nec vestibulum. Sed at tempor ligula. In quis vulputate nunc. Integer at gravida lacus, ac tristique risus. Sed at vulputate nulla.</p>
    <p>Praesent blandit nunc eu efficitur commodo. In tempor nisi ex, vel venenatis ante vestibulum a. Duis vestibulum nibh a erat sagittis, nec euismod lorem varius. Nam ultricies turpis sed justo sollicitudin volutpat. Morbi sed mollis eros. Sed quis tortor id enim vehicula porttitor. Curabitur non aliquam ex. Phasellus dignissim fermentum elit, at finibus ligula mattis eget.</p>
  </section>

  <div class="footer-rule"></div>

  <div class="contact contact-address">
    <div class="contact-row">
      <svg viewBox="0 0 12 12"><path d="M6 0a4 4 0 0 0-4 4c0 3 4 8 4 8s4-5 4-8a4 4 0 0 0-4-4zm0 5.6A1.6 1.6 0 1 1 6 2.4a1.6 1.6 0 0 1 0 3.2z"/></svg>
      <span>suit # 00, Lorem ipsum</span>
    </div>
    <div class="indent">Lorem Lorem ipsum</div>
  </div>
  <span class="divider" style="left:272px"></span>

  <div class="contact contact-phone">
    <div class="contact-row">
      <svg viewBox="0 0 12 12"><path d="M2.5 1l2 2.2-1 1.3a7 7 0 0 0 4 4l1.3-1 2.2 2-1.2 1.5C5.5 11 1 6.5 1 2.2z"/></svg>
      <span>000-000-0000</span>
    </div>
    <div class="contact-row">
      <svg viewBox="0 0 12 12"><path d="M1 4l5-3 5 3v7H1zm1.5 1.2V10h7V5.2L6 7.5z"/></svg>
      <span>000-000-0000</span>
    </div>
  </div>
  <span class="divider" style="left:502px"></span>

  <div class="contact contact-web">
    <div class="contact-row">
      <svg viewBox="0 0 12 12"><path d="M1 4l5-3 5 3v7H1zm1.5 1.2V10h7V5.2L6 7.5z"/></svg>
      <span>info@meridianrealty.com</span>
    </div>
    <div class="contact-row">
      <svg viewBox="0 0 12 12"><path d="M6 .5a5.5 5.5 0 1 0 0 11 5.5 5.5 0 0 0 0-11zm3.9 5H8.2a8 8 0 0 0-.9-3.6A4.3 4.3 0 0 1 9.9 5.5zM6 1.8c.6.8 1 2.2 1.1 3.7H4.9C5 4 5.4 2.6 6 1.8zM4.7 1.9a8 8 0 0 0-.9 3.6H2.1a4.3 4.3 0 0 1 2.6-3.6zM2.1 6.5h1.7a8 8 0 0 0 .9 3.6 4.3 4.3 0 0 1-2.6-3.6zM6 10.2c-.6-.8-1-2.2-1.1-3.7h2.2C7 8 6.6 9.4 6 10.2zm1.3-.1a8 8 0 0 0 .9-3.6h1.7a4.3 4.3 0 0 1-2.6 3.6z"/></svg>
      <span>www.meridianrealty.com</span>
    </div>
  </div>
</main>
</body>
</html>
```